Brightvale Inc. Business Card Design

Brightvale Inc. is in search of a great clean design for our business cards!

Looking to incorporate our full logo and watermark on side one (however, I am open to having the text and watermark separated within the design.)

On side two, I am looking to have contact information (Name, Position, Phone #, Email, Website (www.thebrightvale.ca). Can have the logo and/or watermark as part of the design if applicable.

Please add tagline "Where Shine Counts" on either side 1 or 2. This tagline can be in a sans serif, serif or cursive font as long as it compliments overall design. Capitalization can be title or sentence case depending on how it fits within the design.

Get creative!! Looking for a clean, crisp, premium design! Looking for a glossy card finish with spot UV features when printed. Cards will also be printed with rounded corners. Standard dimensions (3.5 x 2).

Target Market(s)

B2B - primary clients are business owners or property management corporations. (residential jobs are few and far between)

Industry/Entity Type

Business

Contact Information for Business Card

- clean, crisp design
- double sided
- spot UV accents and glossy finish upon printing
- standard business card size (3.5 x 2) with rounded corners
- please see project description for requirements per side

Font styles to use
Sans Serif

Requirements
Must have
• - adequate bleeds with print ready files
• - cohesive design elements between side 1 & 2
• - spot UV elements (can be on both sides or just one, use your discretion)
• - colour pallet should match the logo file provided
• - incorporate tagline "where shine counts" (this tagline can be in a serif or sans serif font as long as it is complimentary to the overall design.
Nice to have
• - Premium elements with a clean design
Should not have
• - Please omit cartoon or whimsical like designs, think premium.
• - Colours should not stray from the pallet of the provided logo.

```html
<!DOCTYPE html>
<html lang="en">
<head>
<meta charset="utf-8">
<title>Brightvale Inc. Business Cards</title>
<link rel="stylesheet" href="https://fonts.googleapis.com/css2?family=Roboto+Condensed:wght@400;700&family=Roboto:ital,wght@0,400;0,700;1,400&display=swap">
<style>
  :root {
    --teal: #1fb5b8;
    --navy: #1b2559;
    --white: #f7f7f7;
    --grey: #55585f;
    --line: #8a8fa8;
    --stage: #e6e8ec;
  }
  * { margin: 0; padding: 0; box-sizing: border-box; }
  html, body { width: 1200px; height: 886px; overflow: hidden; }
  body {
    background: var(--stage);
    font-family: "Roboto", Arial, sans-serif;
    position: relative;
  }
  .card {
    position: absolute;
    border-radius: 18px;
    overflow: hidden;
    background: var(--white);
    box-shadow: 0 10px 28px rgba(20, 30, 60, 0.18);
  }

  /* Side one */
  .card-front { left: 92px; top: 273px; width: 595px; height: 340px; }
  .front-brand {
    position: absolute; left: 0; right: 0; top: 128px;
    display: flex; justify-content: center; align-items: center; gap: 14px;
  }
  .brand-square { width: 34px; height: 34px; background: var(--teal); flex: none; }
  .brand-name {
    font-family: "Roboto Condensed", Arial, sans-serif;
    font-weight: 700; font-size: 46px; letter-spacing: 1px;
    color: var(--navy); text-transform: uppercase; line-height: 1;
    white-space: nowrap;
  }
  .tagline {
    position: absolute; left: 0; right: 0; top: 232px;
    display: flex; justify-content: center; align-items: center; gap: 10px;
    font-style: italic; font-size: 17px; color: var(--navy);
  }
  .tagline .rule { width: 130px; height: 1px; background: var(--line); }
  .tagline .accent { color: var(--teal); }

  /* Side two */
  .card-back { left: 767px; top: 146px; width: 340px; height: 595px; }
  .back-backdrop {
    position: absolute; inset: 0;
    background: linear-gradient(
      to bottom,
      var(--teal) 0%,
      var(--teal) 14%,
      var(--white) 30%,
      var(--white) 80%,
      var(--navy) 100%
    );
  }
  .back-content { position: absolute; left: 80px; top: 190px; right: 24px; color: var(--grey); }
  .back-brand { display: flex; align-items: center; gap: 8px; margin-bottom: 18px; }
  .back-brand .brand-square { width: 20px; height: 20px; }
  .back-brand .brand-name { font-size: 20px; letter-spacing: 0.5px; }
  .person-name {
    font-family: "Roboto Condensed", Arial, sans-serif;
    font-weight: 700; font-size: 31px; color: var(--teal); line-height: 1;
  }
  .person-role {
    font-family: "Roboto Condensed", Arial, sans-serif;
    font-size: 17px; color: var(--navy); margin-top: 4px; letter-spacing: 0.5px;
  }
  .dash { width: 18px; height: 2px; background: var(--teal); margin: 16px 0 14px; }
  .address { font-size: 13.5px; line-height: 1.45; }
  .contact-list { list-style: none; font-size: 13.5px; line-height: 1.45; }
  .contact-list + .contact-list { margin-top: 10px; }
  .label { color: var(--teal); font-weight: 700; }
</style>
</head>
<body>

  <section class="card card-front" aria-label="Business card, side one">
    <div class="front-brand">
      <span class="brand-square"></span>
      <span class="brand-name">Brightvale Inc.</span>
    </div>
    <p class="tagline">
      <span class="rule"></span>
      <span>Where <span class="accent">Shine</span> Counts</span>
      <span class="rule"></span>
    </p>
  </section>

  <section class="card card-back" aria-label="Business card, side two">
    <div class="back-backdrop" role="img" aria-label="Decorative teal and navy background shape framing the contact details"></div>

    <div class="back-content">
      <div class="back-brand">
        <span class="brand-square"></span>
        <span class="brand-name">Brightvale Inc.</span>
      </div>
      <h1 class="person-name">DANIEL REYES</h1>
      <p class="person-role">CEO/FOUNDER</p>
      <div class="dash"></div>
      <p class="address">4120 Cedar Hollow Road<br>Fairbanks, Alaska 99701</p>
      <div class="dash"></div>
      <ul class="contact-list">
        <li><span class="label">P:</span> 555 214 7730</li>
        <li><span class="label">M:</span> 555 386 1942</li>
        <li><span class="label">F:</span> 555 720 4518</li>
      </ul>
      <ul class="contact-list">
        <li><span class="label">E:</span> daniel@thebrightvale.ca</li>
        <li><span class="label">W:</span> www.thebrightvale.ca</li>
      </ul>
    </div>
  </section>

</body>
</html>
```